Dovel Holidays Revamp Project 2015

We are a inbound Travel and tour operator based in Kuala Lumpur, Malaysia, established since 2010. Need a vibrant, dynamic, interactive and user friendly, we expect a Content management system for self data upload.
We cater to different markets around the world form Gulf, to the Far East.
Europe to Africa. With the minimum budget we give maximum services.
The final design should communicate well with the user and portray our growth.

Here is the reference of what our current website looks like.
www.dovelholidays-example.com.my

Target Market(s)

Far-East, South East Asia, Gulf market.

Industry/Entity Type

Travel

Number of Pages Required

5+ page

Font styles to use
Serif
Sans Serif
Other font styles liked:
• Calibri

Requirements
Must have
• User interaction, User friendly, Payment integration, should have a fun interface.
Should not have
• Should not have a complicated and overcrowded or jumbled up layout.

```html
<!DOCTYPE html>
<html lang="en">
<head>
<meta charset="utf-8">
<title>Dovel Holidays</title>
<link href="https://fonts.googleapis.com/css2?family=Open+Sans:ital,wght@0,400;0,600;0,700;1,400&display=swap" rel="stylesheet">
<style>
:root{
  --red:#b5151f;
  --red-dark:#8f0f17;
  --ink:#222;
  --text:#666;
  --muted:#999;
  --band:#444;
  --dark:#2b2b2b;
  --footer:#333;
  --light:#e6e6e6;
  --white:#fff;
}
*{box-sizing:border-box;margin:0;padding:0}
html,body{width:1200px;height:2932px;overflow:hidden;background:var(--white)}
body{font-family:"Open Sans",Arial,sans-serif;color:var(--text);position:relative}
.abs{position:absolute}
section,header,footer{position:absolute;left:0;width:1200px}

/* header */
.site-header{top:0;height:141px}
.brand{left:100px;top:34px;display:flex;align-items:center;gap:12px}
.brand-dot{width:44px;height:44px;border-radius:50%;background:var(--red)}
.brand-name{font-size:27px;font-weight:700;color:var(--red)}
.contact-top{right:142px;top:34px;text-align:right}
.contact-top .mail{font-size:13px;color:#444}
.contact-top .tel{font-size:20px;font-weight:700;color:var(--red);line-height:30px}
.phone-icon{left:1065px;top:44px;width:33px;height:33px;border-radius:50%;background:#444;display:flex;align-items:center;justify-content:center}

/* nav */
.main-nav{position:absolute;left:98px;top:117px;width:1002px;height:45px;background:var(--red);display:flex;z-index:3}
.main-nav a{color:var(--white);font-size:13px;text-decoration:none;display:flex;align-items:center;padding:0 23px;border-right:1px solid var(--red-dark)}
.main-nav a.active{background:var(--red-dark)}
.nav-search{position:absolute;right:10px;top:6px;width:236px;height:33px;background:var(--white);display:flex;align-items:center;justify-content:space-between;padding:0 12px;font-size:11px;color:var(--muted)}

/* hero */
.hero{top:141px;height:518px;background:linear-gradient(180deg,#c9c3b3 0%,#bdb4a1 40%,#9b8a70 75%,#7c6a52 100%)}
.hero h1{position:absolute;left:98px;top:142px;font-size:23px;font-weight:600;color:var(--ink)}
.slide-arrow{position:absolute;top:240px;width:28px;height:36px;background:rgba(60,60,60,.75);display:flex;align-items:center;justify-content:center}

/* search band */
.finder{top:659px;height:137px;background:var(--band)}
.finder label{position:absolute;top:42px;color:var(--white);font-size:14px}
.finder .field{position:absolute;top:64px;height:35px;background:var(--white);font-size:11px;color:var(--muted);display:flex;align-items:center;justify-content:space-between;padding:0 12px}
.finder .go{position:absolute;left:921px;top:64px;width:92px;height:35px;background:var(--red);color:var(--white);font-size:13px;font-weight:600;display:flex;align-items:center;justify-content:center}

/* experience */
.experience{top:796px;height:369px}
.experience h2{position:absolute;left:113px;top:58px;font-size:27px;font-weight:600;color:var(--red)}
.lead{position:absolute;left:113px;top:106px;width:560px;font-size:14px;line-height:23px;color:var(--ink)}
.intro{position:absolute;left:113px;top:160px;width:540px;font-size:12px;line-height:22px}
.testimonial{position:absolute;left:688px;top:115px;width:397px;height:120px;border:1px solid #ddd;padding:14px 26px 0 62px;font-style:italic;font-size:12.5px;line-height:22px;color:var(--muted)}
.testimonial .q{position:absolute;font-size:34px;font-style:normal;font-weight:700;color:#bbb;line-height:1}
.testimonial .tail{position:absolute;right:34px;bottom:-12px;width:22px;height:22px;background:var(--white);border-right:1px solid #ddd;border-bottom:1px solid #ddd;transform:rotate(45deg)}
.cite{position:absolute;right:117px;top:280px;font-size:12px;color:var(--red)}

/* best offers */
.best{top:1165px;height:549px;background:var(--dark)}
.best h2{position:absolute;top:46px;width:100%;text-align:center;font-size:31px;font-weight:700;color:var(--white)}
.best .sub{position:absolute;top:90px;width:100%;text-align:center;font-size:11px;color:#aaa;letter-spacing:.5px}
.offer{position:absolute;top:153px;width:326px;height:336px;background:var(--white)}
.offer .photo{height:236px}
.offer h3{text-align:center;font-size:15px;font-weight:600;color:var(--ink);margin-top:21px}
.offer p{text-align:center;font-size:12px;color:var(--red);line-height:21px}
.side-arrow{position:absolute;width:24px;height:24px}

/* more offers */
.more{top:1714px;height:264px;background:var(--light)}
.more h2{position:absolute;top:32px;width:100%;text-align:center;font-size:14px;font-weight:600;color:#777}
.thumb{position:absolute;top:71px;width:243px;height:158px}

/* why / news */
.why{top:1978px;height:544px}
.why h2,.news h2{position:absolute;top:72px;font-size:26px;font-weight:600;color:var(--red)}
.reason{position:absolute;left:113px;width:480px}
.reason .badge{position:absolute;left:0;top:0;width:43px;height:78px;background:var(--red);display:flex;align-items:center;justify-content:center}
.reason h3{margin-left:55px;font-size:14px;font-weight:600;color:var(--ink);line-height:20px}
.reason p{margin-left:55px;font-size:11.5px;line-height:20px;color:var(--text)}
.news-box{position:absolute;left:630px;top:118px;width:453px;height:348px;border:1px solid #ddd}
.story{position:absolute;left:18px;width:415px}
.story .pic{position:absolute;left:0;top:0;width:129px;height:128px}
.story h3{margin-left:146px;font-size:13px;font-weight:600;color:var(--ink);line-height:20px}
.story .date{margin-left:146px;font-size:11px;color:#555;line-height:20px}
.story p{margin-left:146px;margin-top:8px;font-size:11px;line-height:19.5px;color:var(--muted)}
.news-divider{position:absolute;left:18px;top:172px;width:415px;border-top:1px solid #ddd}

/* contact strip */
.contact-strip{top:2522px;height:98px;background:var(--light)}
.contact-strip .col{position:absolute;top:28px;font-size:11.5px;line-height:19.5px;color:#444}
.contact-strip .col b{font-weight:400;color:#555}
.contact-strip .val{color:#1d3f8f}
.partner{position:absolute;top:18px;height:62px;border-radius:4px}

/* footer */
.site-footer{top:2620px;height:312px;background:var(--footer)}
.links{position:absolute;top:37px;height:180px;padding-left:0}
.links h4{font-size:13px;font-weight:400;color:var(--white);margin-bottom:8px}
.links li{list-style:none;font-size:11px;color:#999;line-height:22.5px}
.col-rule{position:absolute;top:40px;height:160px;border-left:1px solid #4a4a4a}
.footer-rule{position:absolute;left:100px;top:234px;width:1000px;border-top:1px solid #4a4a4a}
.copyright{position:absolute;left:100px;top:266px;font-size:10.5px;color:#ccc}
.social{position:absolute;left:796px;top:258px;display:flex;gap:2px}
.social span{width:32px;height:32px;border-radius:50%;background:#5d5d5d;display:block}
.to-top{position:absolute;left:1070px;top:257px;width:34px;height:34px;border-radius:50%;border:2px solid #888;display:flex;align-items:center;justify-content:center}
</style>
</head>
<body>

<header class="site-header">
  <div class="abs brand"><span class="brand-dot"></span><span class="brand-name">Dovel Holidays</span></div>
  <div class="abs contact-top">
    <div class="mail">tours@dovelholidays-example.com.my</div>
    <div class="tel">00-60312345670</div>
  </div>
  <div class="abs phone-icon">
    <svg width="16" height="16" viewBox="0 0 24 24"><path fill="#fff" d="M6.6 10.8a15 15 0 0 0 6.6 6.6l2.2-2.2c.3-.3.7-.4 1-.2 1.1.4 2.3.6 3.6.6.6 0 1 .4 1 1V20c0 .6-.4 1-1 1A17 17 0 0 1 3 4c0-.6.4-1 1-1h3.5c.6 0 1 .4 1 1 0 1.3.2 2.5.6 3.6.1.3 0 .7-.2 1z"/></svg>
  </div>
</header>

<nav class="main-nav">
  <a class="active" href="#">Home</a>
  <a href="#">About us</a>
  <a href="#">Tours</a>
  <a href="#">Pay Bills</a>
  <a href="#">Contact us</a>
  <div class="nav-search"><span>Search</span>
    <svg width="12" height="12" viewBox="0 0 24 24"><circle cx="10" cy="10" r="7" fill="none" stroke="#777" stroke-width="3"/><path d="M15 15l6 6" stroke="#777" stroke-width="3"/></svg>
  </div>
</nav>

<section class="hero" role="img" aria-label="City skyline of Kuala Lumpur with twin towers under a hazy sky">
  <h1>Bringing Group Travel To A Higher Standard</h1>
  <div class="slide-arrow" style="left:0"><svg width="10" height="14"><path d="M8 1L2 7l6 6" fill="none" stroke="#fff" stroke-width="2"/></svg></div>
  <div class="slide-arrow" style="right:0"><svg width="10" height="14"><path d="M2 1l6 6-6 6" fill="none" stroke="#fff" stroke-width="2"/></svg></div>
</section>

<section class="finder">
  <label style="left:186px">Destination</label>
  <div class="field" style="left:186px;width:226px">City, region or keywords</div>
  <label style="left:444px">Date</label>
  <div class="field" style="left:444px;width:88px">From <svg width="12" height="12"><rect x="1" y="2" width="10" height="9" fill="none" stroke="#aaa"/><path d="M1 5h10" stroke="#aaa"/></svg></div>
  <div class="field" style="left:538px;width:88px">To <svg width="12" height="12"><rect x="1" y="2" width="10" height="9" fill="none" stroke="#aaa"/><path d="M1 5h10" stroke="#aaa"/></svg></div>
  <label style="left:665px">Max Budget</label>
  <div class="field" style="left:665px;width:227px">USD EX 100</div>
  <div class="go">SEARCH</div>
</section>

<section class="experience">
  <h2>A World of Experience</h2>
  <p class="lead">“Beautiful beaches, world- class infrastructure, mangroves rich in flora and fauna, ultra- cheap duty-free shopping and fascinating legends.”</p>
  <p class="intro">For a once in a lifetime experience, take an Dovel Holidays tour and discover the wonders of Malaysia – one of Asia’s top holiday destinations. From pristine rainforests to silvery sand beaches and from sleek cityscapes to the rural wilds, this beautiful country brings together all the ingredients for a perfect holiday. All this, along with its friendly people and exciting cultures, it’s hardly surprising that Malaysia has it all. As there is an incredible amount to see and do, we’ve picked out the best excursions so you don’t miss the highlights.</p>
  <blockquote class="testimonial">
    <span class="q" style="left:24px;top:12px">“</span>
    Proin porta fermentum ipsum, vel porttitor turpis venenatis luctus. Vivamus volutpat eu sapien quis tempus, Aenean feugiat viverra lorem ac sagittis.
    <span class="q" style="left:286px;top:82px">”</span>
    <span class="tail"></span>
  </blockquote>
  <div class="cite">Mark Ansel</div>
</section>

<section class="best">
  <h2>BEST OFFERS</h2>
  <div class="sub">CHECK OUT OUR BEST PROMOTION TOURS</div>
  <svg class="side-arrow" style="left:22px;top:305px" viewBox="0 0 24 24"><path d="M15 3L6 12l9 9" fill="none" stroke="#888" stroke-width="2"/></svg>
  <svg class="side-arrow" style="left:1154px;top:305px" viewBox="0 0 24 24"><path d="M9 3l9 9-9 9" fill="none" stroke="#888" stroke-width="2"/></svg>
  <article class="offer" style="left:100px">
    <div class="photo" role="img" aria-label="Tropical island bay with turquoise water and green hills" style="background:linear-gradient(180deg,#4a78b8 0%,#6f9c6a 45%,#2fb3a8 70%,#1f8a8f 100%)"></div>
    <h3>3 Nights Malaysia Package</h3>
    <p>2 Nights Harbour Inn, Kuala lumpur<br>1 Night Summit View, Genting Highlands</p>
  </article>
  <article class="offer" style="left:436px">
    <div class="photo" role="img" aria-label="Kuala Lumpur tower and heritage buildings lit at dusk" style="background:linear-gradient(180deg,#2a3a8a 0%,#3d4fa0 50%,#7a5a48 80%,#3a2a22 100%)"></div>
    <h3>3 Nights Malaysia Package</h3>
    <p>2 Nights Harbour Inn, Kuala lumpur<br>1 Night Summit View, Genting Highlands</p>
  </article>
  <article class="offer" style="left:774px">
    <div class="photo" role="img" aria-label="Beach resort with sun loungers and palm trees" style="background:linear-gradient(180deg,#9dc4e0 0%,#5f8f5a 40%,#c8b9a0 75%,#e2d6c2 100%)"></div>
    <h3>3 Nights Malaysia Package</h3>
    <p>2 Nights Harbour Inn, Kuala lumpur<br>1 Night Summit View, Genting Highlands</p>
  </article>
</section>

<section class="more">
  <h2>MORE OFFERS</h2>
  <svg class="side-arrow" style="left:20px;top:118px" viewBox="0 0 24 24"><path d="M15 3L6 12l9 9" fill="none" stroke="#999" stroke-width="2"/></svg>
  <svg class="side-arrow" style="left:1156px;top:118px" viewBox="0 0 24 24"><path d="M9 3l9 9-9 9" fill="none" stroke="#999" stroke-width="2"/></svg>
  <div class="thumb" style="left:100px;background:linear-gradient(180deg,#8aa0b8,#5f7a58 55%,#9a8c7a)" role="img" aria-label="Hillside theme park resort"></div>
  <div class="thumb" style="left:352px;background:linear-gradient(180deg,#5d95d0,#3f7a55 45%,#2fbfb8 75%,#8a7a66)" role="img" aria-label="Wooden jetty over clear turquoise sea"></div>
  <div class="thumb" style="left:604px;background:linear-gradient(180deg,#4c7a6a,#2aa5b0 40%,#38b8c0 100%)" role="img" aria-label="Clear shallow water by a tropical island"></div>
  <div class="thumb" style="left:856px;background:linear-gradient(180deg,#a0c4d8,#4f7f6a 45%,#3aa8a8 80%,#2f8890)" role="img" aria-label="Longtail boat on a lagoon below limestone cliffs"></div>
</section>

<section class="why">
  <h2 style="left:113px">WHY CHOOSE US</h2>
  <div class="reason" style="top:114px">
    <div class="badge"><svg width="18" height="18" viewBox="0 0 24 24"><path fill="#fff" d="M12 2l3 7h7l-5.5 4.5 2 7.5L12 16.5 5.5 21l2-7.5L2 9h7z"/></svg></div>
    <h3>Our aim</h3>
    <p>Help our trade partners sell better than their competitors and our travel clients with a memorable trip. We strive to provide that delicate balance between competitive pricing, quality products and personalized customer service.</p>
  </div>
  <div class="reason" style="top:239px">
    <div class="badge"><svg width="18" height="18" viewBox="0 0 24 24"><circle cx="12" cy="12" r="9" fill="#fff"/><path d="M7 9c2 0 3 1 3 3s2 3 2 5M14 5c0 2 2 3 4 3" stroke="#b5151f" stroke-width="1.6" fill="none"/></svg></div>
    <h3>Pricing &amp; quality service</h3>
    <p>Persistent efforts are in place to:<br>• continue upgrading of customer service/handling skills<br>• source for quality suppliers &amp; products<br>• own fleet of vehicles in Malaysia (coaches &amp; vans)</p>
  </div>
  <div class="reason" style="top:368px">
    <div class="badge"><svg width="18" height="18" viewBox="0 0 24 24"><path fill="#fff" d="M2 10h4v11H2zM8 10l4-8c2 0 3 1 3 3l-1 4h6c1 0 2 1 2 2l-2 8c-.2.6-.8 1-1.5 1H8z"/></svg></div>
    <h3>Tour Fleet</h3>
    <p>For sightseeing or shopping, for touring or for transfers – Dovel Holidays has just the vehicle for you. From the best executives sedans to minibuses to full-sized luxury motorcoaches, we have the right vehicle for the right experience.</p>
  </div>

  <h2 style="left:628px">Latest News</h2>
  <svg class="abs" style="left:1062px;top:76px" width="22" height="22" viewBox="0 0 24 24"><circle cx="12" cy="12" r="10" fill="none" stroke="#555" stroke-width="1.6"/><path d="M7 12h9M12 8l4 4-4 4" fill="none" stroke="#555" stroke-width="1.6"/></svg>
  <div class="news-box">
    <article class="story" style="top:17px">
      <div class="pic" role="img" aria-label="Aerial view of an island coastline" style="background:linear-gradient(180deg,#8aa6c0,#4f7d5a 50%,#3fb0aa)"></div>
      <h3>Proin a dolor mauris</h3>
      <div class="date">April 15, 2015</div>
      <p>Nunc sit amet consequat risus. Curabitur ac elit leo. In eleifend dui tellus, in scelerisque elit porttitor et. Integer eu massa lacinia, lacinia nulla non, volutpat purus. Sed libero felis, vestibulum et.</p>
    </article>
    <div class="news-divider"></div>
    <article class="story" style="top:197px">
      <div class="pic" role="img" aria-label="Colonial-era building with domes in the city" style="background:linear-gradient(180deg,#6f9ad0,#c7b79a 55%,#6a5a48)"></div>
      <h3>Proin a dolor mauris</h3>
      <div class="date">April 15, 2015</div>
      <p>Nunc sit amet consequat risus. Curabitur ac elit leo. In eleifend dui tellus, in scelerisque elit porttitor et. Integer eu massa lacinia, lacinia nulla non, volutpat purus. Sed libero felis, vestibulum et.</p>
    </article>
  </div>
</section>

<section class="contact-strip">
  <div class="col" style="left:111px"><b>Address</b><br><span class="val">Suite No. 3-07 , 5th Floor Wisma Seri Angkasa<br>No.41 Jalan Melati Indah Kuala Lumpur . Malaysia.</span></div>
  <div class="col" style="left:420px"><b>Phone</b><br><span class="val">00-60312345678<br>00-60312345670</span></div>
  <div class="col" style="left:567px"><b>E-mail</b><br><span class="val">tours@dovelholidays-example.com.my</span></div>
  <div class="partner" style="left:790px;width:136px;background:#c9ccd6"></div>
  <div class="partner" style="left:972px;width:108px;background:#c9ccd6"></div>
</section>

<footer class="site-footer">
  <ul class="links" style="left:100px"><h4>Quick Links</h4><li>Home</li><li>About us</li><li>Tours</li><li>Pay Bills</li><li>Contact us</li><li>Faq.</li></ul>
  <div class="col-rule" style="left:232px"></div>
  <ul class="links" style="left:270px"><h4>Support</h4><li>Register</li><li>Login</li><li>Help</li><li>Etiam et magna</li><li>Nunc porttitor</li><li>Phasellus</li></ul>
  <div class="col-rule" style="left:406px"></div>
  <ul class="links" style="left:455px"><h4>Other Links</h4><li>Pellentesque id</li><li>Suspendisse</li><li>Donec nec</li><li>Etiam et magna</li><li>Nunc porttitor</li><li>Phasellus</li></ul>
  <div class="col-rule" style="left:596px"></div>
  <ul class="links" style="left:641px"><h4>Other Links</h4><li>Pellentesque id</li><li>Suspendisse</li><li>Donec nec</li><li>Etiam et magna</li><li>Nunc porttitor</li><li>Phasellus</li></ul>
  <div class="col-rule" style="left:784px"></div>
  <ul class="links" style="left:829px"><h4>Other Links</h4><li>Pellentesque id</li><li>Suspendisse</li><li>Donec nec</li><li>Etiam et magna</li><li>Nunc porttitor</li><li>Phasellus</li></ul>
  <div class="col-rule" style="left:972px"></div>
  <ul class="links" style="left:1015px"><h4>Other Links</h4><li>Pellentesque id</li><li>Suspendisse</li><li>Donec nec</li><li>Etiam et magna</li><li>Nunc porttitor</li><li>Phasellus</li></ul>
  <div class="footer-rule"></div>
  <div class="copyright">Copyright &nbsp;© 2015 &nbsp;Dovel Holidays. &nbsp;All rights reserved.</div>
  <div class="social"><span></span><span></span><span></span><span></span><span></span><span></span><span></span><span></span></div>
  <div class="to-top"><svg width="14" height="14" viewBox="0 0 24 24"><path d="M12 20V5M5 12l7-7 7 7" fill="none" stroke="#aaa" stroke-width="2.5"/></svg></div>
</footer>

</body>
</html>
```